Gilded Realty website

full website from start to finish. I would like something like this -
https://www.brindlecovemanors.com/
http://plumhavenlots.com/

Target Market(s)

real estate investors

Industry/Entity Type

Real Estate

Number of Pages Required

5+ page

Font styles to use
Sans Serif

Colors

Designer to choose colors to be used in the design.

Requirements
Must have
• translated in English, Spanish and japanese

```html
<!DOCTYPE html>
<html lang="en">
<head>
<meta charset="utf-8">
<title>Gilded Realty</title>
<link href="https://fonts.googleapis.com/css2?family=Montserrat:wght@300;400;500;600;700&display=swap" rel="stylesheet">
<style>
:root{
  --accent:#27b58d;
  --ink:#222629;
  --muted:#7d8287;
  --line:#e4e6e8;
  --soft:#f4f5f6;
  --page:#f0f1f2;
  --dark:#1d2124;
  --footer:#202427;
  --white:#ffffff;
}
*{margin:0;padding:0;box-sizing:border-box}
html,body{width:1200px;height:5158px;overflow:hidden}
body{font-family:"Montserrat",sans-serif;color:var(--ink);background:var(--white);position:relative}
.section{position:absolute;left:0;width:1200px}
.section-title{text-align:center;font-size:30px;font-weight:400;letter-spacing:4px;text-transform:uppercase}
.title-dots{display:flex;gap:6px;justify-content:center;margin-top:12px}
.title-dots span{width:7px;height:7px;border-radius:50%;background:var(--accent)}

/* hero */
.hero{top:0;height:557px;background:linear-gradient(180deg,#3b4658 0%,#5b5a6b 35%,#7d6552 62%,#3e4b59 82%,#2c5f85 100%)}
.nav{position:absolute;top:30px;left:96px;right:96px;display:flex;align-items:center;color:var(--white)}
.brand{font-weight:700;font-size:19px;letter-spacing:1px;text-transform:uppercase}
.menu{margin-left:auto;display:flex;gap:28px;font-size:14px;font-weight:500}
.menu a{color:var(--white);text-decoration:none}
.phone{margin-left:58px;display:flex;align-items:center;gap:12px;font-size:15px;font-weight:500}
.lang{margin-left:38px;display:flex;align-items:center;gap:6px}
.lang i{display:block;width:20px;height:13px;background:#e8e8ea;border:1px solid #c04040}
.hero-title{position:absolute;top:222px;width:100%;text-align:center;color:var(--white);font-size:46px;font-weight:400;letter-spacing:1px}
.play{position:absolute;top:285px;left:580px;width:40px;height:40px;border-radius:50%;background:var(--white)}

/* about */
.about{top:557px;height:613px;background:var(--page)}
.about-text{position:absolute;left:96px;top:138px;width:430px}
.about-text h2{font-size:28px;font-weight:500;letter-spacing:2px;text-transform:uppercase;margin-bottom:18px}
.about-text p{font-size:12.5px;line-height:24px;color:var(--muted)}
.btn{display:inline-block;margin-top:28px;background:var(--accent);color:var(--white);font-size:12px;font-weight:600;padding:14px 22px;text-transform:uppercase}
.about-photo{position:absolute;left:612px;top:117px;width:488px;height:375px;background:linear-gradient(135deg,#eceae6,#cfcbc4 60%,#9f8a72)}

/* properties */
.properties{top:1170px;height:1238px;background:var(--white)}
.properties .section-title{margin-top:108px}
.prop-grid{position:absolute;left:96px;top:213px;width:1004px;display:grid;grid-template-columns:repeat(3,1fr);column-gap:14px;row-gap:21px}
.prop-card{border:1px solid var(--line);height:447px;background:var(--white)}
.prop-photo{height:215px}
.prop-body{padding:16px 14px 12px}
.prop-body h3{font-size:16px;font-weight:600}
.prop-body p{font-size:10.5px;color:var(--muted);margin-top:4px}
.prop-row{display:flex;justify-content:space-between;font-size:11.5px;padding:12px 14px;height:38px}
.prop-row:nth-child(odd){background:var(--soft)}
.prop-row b{font-weight:500;color:var(--muted)}

/* benefits */
.benefits{top:2408px;height:440px;background:linear-gradient(180deg,#262a2e,#1b1f22);color:var(--white)}
.benefits .section-title{margin-top:108px;font-size:28px}
.benefit-row{position:absolute;top:174px;left:96px;width:1004px;display:grid;grid-template-columns:repeat(3,1fr);text-align:center}
.benefit-row svg{margin:0 auto 14px;display:block}
.benefit-row h3{font-size:19px;font-weight:400;margin-bottom:12px}
.benefit-row p{font-size:11.5px;line-height:20px;color:#b8bcc0;width:270px;margin:0 auto}

/* gallery */
.gallery{top:2848px;height:1039px;background:var(--page)}
.gallery .section-title{margin-top:115px;font-size:28px}
.tabs{position:absolute;top:196px;left:0;width:100%;display:flex;justify-content:center;gap:26px;font-size:13px}
.tabs span{padding:6px 0}
.tabs .active{background:var(--accent);color:var(--white);padding:6px 22px;margin-right:8px}
.tile{position:absolute}
.tile .zoom{position:absolute;left:0;bottom:0;width:34px;height:34px;background:var(--accent)}

/* testimonials */
.testimonials{top:3887px;height:516px;background:linear-gradient(90deg,#6b4a31,#b88a5c 30%,#d9c0a0 55%,#7a5a43 85%,#4a3526)}
.quote-card{position:absolute;top:86px;width:327px;height:293px;background:var(--white);padding:50px 26px 0}
.quote-mark{position:absolute;top:-20px;left:26px;width:40px;height:40px;background:var(--accent)}
.quote-card h3{font-size:16px;font-weight:600;margin-bottom:14px}
.quote-card p{font-size:11px;line-height:19px;color:var(--muted)}
.quote-foot{position:absolute;left:26px;right:26px;bottom:26px;display:flex;justify-content:space-between;align-items:center}
.quote-foot b{color:var(--accent);font-size:14px;font-weight:500}
.quote-foot span{font-size:10px;color:var(--muted)}

/* partners */
.partners{top:4403px;height:379px;background:var(--white)}
.partners .section-title{margin-top:108px;font-size:28px}
.partner-row{position:absolute;top:196px;left:120px;width:960px;display:flex;justify-content:space-between;align-items:center}
.partner-badge{width:130px;height:56px;border-radius:6px;background:#e2e4e6}

/* footer */
.footer{top:4782px;height:376px;background:var(--footer);color:var(--white)}
.foot-col{position:absolute;top:60px}
.foot-col h4{font-size:19px;font-weight:400;margin-bottom:24px}
.foot-col .label{font-size:14px;margin-top:8px}
.foot-col .val{font-size:10.5px;color:#a9adb1;margin-top:4px}
.foot-col ul{list-style:none;font-size:10.5px;color:#a9adb1;line-height:22px}
.subscribe{display:flex;margin-top:14px;width:276px}
.subscribe div{flex:1;height:36px;background:var(--white);font-size:10px;color:var(--muted);padding:12px 10px}
.subscribe span{width:36px;height:36px;background:var(--accent)}
.socials{display:flex;gap:12px;margin-top:18px}
.socials i{width:26px;height:26px;border-radius:50%;background:var(--accent);display:block}
.copyright{position:absolute;bottom:0;left:0;width:100%;height:40px;border-top:1px solid #33383c;text-align:center;font-size:10px;color:#8a8f94;padding-top:14px}
.copyright b{color:var(--accent);font-weight:500}
</style>
</head>
<body>

<header class="section hero" role="img" aria-label="Photo of a luxury villa lit at dusk with a pool in front">
  <nav class="nav">
    <div class="brand">Gilded Realty</div>
    <div class="menu"><a>Home</a><a>About Us</a><a>Our Properties</a><a>Contact Us</a></div>
    <div class="phone">
      <svg width="16" height="16" viewBox="0 0 24 24" fill="#fff"><path d="M6.6 10.8a15 15 0 0 0 6.6 6.6l2.2-2.2a1 1 0 0 1 1-.25 11.4 11.4 0 0 0 3.6.57 1 1 0 0 1 1 1V20a1 1 0 0 1-1 1A17 17 0 0 1 3 4a1 1 0 0 1 1-1h3.5a1 1 0 0 1 1 1c0 1.25.2 2.45.57 3.57a1 1 0 0 1-.25 1z"/></svg>
      555-014-7230
    </div>
    <div class="lang"><i></i><svg width="8" height="5" viewBox="0 0 8 5"><path d="M0 0h8L4 5z" fill="#fff"/></svg></div>
  </nav>
  <h1 class="hero-title">Gilded Realty</h1>
  <div class="play"><svg width="40" height="40" viewBox="0 0 40 40"><path d="M16 12l12 8-12 8z" fill="#222"/></svg></div>
</header>

<section class="section about">
  <div class="about-text">
    <h2>Gilded Realty</h2>
    <p>Sed ut perspiciatis unde omnis iste natus error sit voluptatem accusantium doloremque laudantium, totam rem aperiam, eaque ipsa quae ab illo inventore veritatis et quasi architecto beatae vitae dicta sunt explicabo. Nemo enim ipsam voluptatem quia voluptas sit aspernatur aut odit aut fugit, sed quia consequuntur magni dolores eos qui ratione voluptatem sequi nesciunt. Neque porro quisquam est, qui dolorem ipsum quia dolor sit amet, consectetur, adipisci velit, sed quia non numquam eius modi tempora incidunt ut labore et dolore magnam aliquam quaerat.</p>
    <span class="btn">Read More</span>
  </div>
  <div class="about-photo" role="img" aria-label="Photo of a bright white kitchen with pendant lamps and flowers"></div>
</section>

<section class="section properties">
  <h2 class="section-title">Our Properties</h2>
  <div class="title-dots"><span></span><span></span><span></span></div>
  <div class="prop-grid">
    <article class="prop-card"><div class="prop-photo" role="img" aria-label="Photo of a modern red and white house at sunset" style="background:linear-gradient(135deg,#e0623a,#b8232a 50%,#3a3f52)"></div><div class="prop-body"><h3>Lorem ipsum dolor sit amet</h3><p>Sed ut perspiciatis unde omnis iste natus error</p></div><div><div class="prop-row"><b>Price</b><span>$550,000</span></div><div class="prop-row"><b>Area</b><span>124 M²</span></div><div class="prop-row"><b>Bedrooms</b><span>3</span></div><div class="prop-row"><b>Bathrooms</b><span>2</span></div></div></article>
    <article class="prop-card"><div class="prop-photo" role="img" aria-label="Photo of a bedroom with a yellow throw" style="background:linear-gradient(135deg,#4b4338,#8a7a5a 50%,#d8b23a)"></div><div class="prop-body"><h3>Lorem ipsum dolor sit amet</h3><p>Sed ut perspiciatis unde omnis iste natus error</p></div><div><div class="prop-row"><b>Price</b><span>$550,000</span></div><div class="prop-row"><b>Area</b><span>124 M²</span></div><div class="prop-row"><b>Bedrooms</b><span>3</span></div><div class="prop-row"><b>Bathrooms</b><span>2</span></div></div></article>
    <article class="prop-card"><div class="prop-photo" role="img" aria-label="Photo of a hallway with a dark wooden door" style="background:linear-gradient(135deg,#d9cbb4,#a88a62 55%,#3b2e25)"></div><div class="prop-body"><h3>Lorem ipsum dolor sit amet</h3><p>Sed ut perspiciatis unde omnis iste natus error</p></div><div><div class="prop-row"><b>Price</b><span>$550,000</span></div><div class="prop-row"><b>Area</b><span>124 M²</span></div><div class="prop-row"><b>Bedrooms</b><span>3</span></div><div class="prop-row"><b>Bathrooms</b><span>2</span></div></div></article>
    <article class="prop-card"><div class="prop-photo" role="img" aria-label="Photo of a grey modern kitchen" style="background:linear-gradient(135deg,#5d6166,#9a9ea3 50%,#3a3d41)"></div><div class="prop-body"><h3>Lorem ipsum dolor sit amet</h3><p>Sed ut perspiciatis unde omnis iste natus error</p></div><div><div class="prop-row"><b>Price</b><span>$550,000</span></div><div class="prop-row"><b>Area</b><span>124 M²</span></div><div class="prop-row"><b>Bedrooms</b><span>3</span></div><div class="prop-row"><b>Bathrooms</b><span>2</span></div></div></article>
    <article class="prop-card"><div class="prop-photo" role="img" aria-label="Photo of a glass-fronted house lit at dusk" style="background:linear-gradient(160deg,#4a5c86,#8e7d8c 45%,#e0a062 75%,#4b4a52)"></div><div class="prop-body"><h3>Lorem ipsum dolor sit amet</h3><p>Sed ut perspiciatis unde omnis iste natus error</p></div><div><div class="prop-row"><b>Price</b><span>$550,000</span></div><div class="prop-row"><b>Area</b><span>124 M²</span></div><div class="prop-row"><b>Bedrooms</b><span>3</span></div><div class="prop-row"><b>Bathrooms</b><span>2</span></div></div></article>
    <article class="prop-card"><div class="prop-photo" role="img" aria-label="Photo of a villa pool with palm trees at twilight" style="background:linear-gradient(180deg,#7a8fb0,#c9a07e 45%,#2f5f86 70%,#1c3a58)"></div><div class="prop-body"><h3>Lorem ipsum dolor sit amet</h3><p>Sed ut perspiciatis unde omnis iste natus error</p></div><div><div class="prop-row"><b>Price</b><span>$550,000</span></div><div class="prop-row"><b>Area</b><span>124 M²</span></div><div class="prop-row"><b>Bedrooms</b><span>3</span></div><div class="prop-row"><b>Bathrooms</b><span>2</span></div></div></article>
  </div>
</section>

<section class="section benefits">
  <h2 class="section-title">Benefits</h2>
  <div class="title-dots"><span></span><span></span><span></span></div>
  <div class="benefit-row">
    <div>
      <svg width="40" height="40" viewBox="0 0 40 40" fill="none" stroke="#27b58d" stroke-width="2"><path d="M5 20L20 7l15 13"/><path d="M10 16v17h20V16"/><path d="M17 33v-9h6v9"/></svg>
      <h3>Hottest Property List</h3>
      <p>Sed ut perspiciatis unde omnis iste natus error sit voluptatem accusantium doloremque laudantium, totam rem aperiam.</p>
    </div>
    <div>
      <svg width="40" height="40" viewBox="0 0 40 40" fill="none" stroke="#27b58d" stroke-width="2"><circle cx="20" cy="20" r="15"/><path d="M24 14.5c-1-1.3-2.5-1.8-4-1.8-2.3 0-4 1.2-4 3.2 0 4.4 8.3 2.4 8.3 7 0 2-1.8 3.3-4.3 3.3-1.7 0-3.2-.6-4.3-1.9M20 10v20"/></svg>
      <h3>Best Price In market</h3>
      <p>Sed ut perspiciatis unde omnis iste natus error sit voluptatem accusantium doloremque laudantium, totam rem aperiam.</p>
    </div>
    <div>
      <svg width="40" height="40" viewBox="0 0 40 40" fill="none" stroke="#27b58d" stroke-width="2"><circle cx="20" cy="15" r="9"/><circle cx="20" cy="15" r="4"/><path d="M14 22l-3 12 5-3 3 4M26 22l3 12-5-3-3 4"/></svg>
      <h3>Guaranteed Service</h3>
      <p>Sed ut perspiciatis unde omnis iste natus error sit voluptatem accusantium doloremque laudantium, totam rem aperiam.</p>
    </div>
  </div>
</section>

<section class="section gallery">
  <h2 class="section-title">Gilded Realty</h2>
  <div class="tabs"><span class="active">All</span><span>Bed Room</span><span>Living Room</span><span>Kitchen</span><span>Garage</span><span>Basement</span></div>
  <div class="tile" style="left:96px;top:289px;width:317px;height:193px;background:linear-gradient(135deg,#dcd8d0,#b0a08a)" role="img" aria-label="Photo of a kitchen with a wooden island"><i class="zoom"></i></div>
  <div class="tile" style="left:96px;top:505px;width:317px;height:196px;background:linear-gradient(135deg,#f2f2f0,#c8d0c4)" role="img" aria-label="Photo of a white living room with plants"><i class="zoom"></i></div>
  <div class="tile" style="left:96px;top:730px;width:317px;height:196px;background:linear-gradient(135deg,#5a4a3e,#c9b7a0)" role="img" aria-label="Photo of a bedroom with wooden beams"><i class="zoom"></i></div>
  <div class="tile" style="left:433px;top:289px;width:667px;height:320px;background:linear-gradient(135deg,#f6f6f6,#dedfe0 60%,#c9a77c)" role="img" aria-label="Photo of a white kitchen counter with a potted plant"><i class="zoom"></i></div>
  <div class="tile" style="left:433px;top:730px;width:323px;height:196px;background:linear-gradient(135deg,#efefed,#c7c1b6)" role="img" aria-label="Photo of a bright dining area"><i class="zoom"></i></div>
  <div class="tile" style="left:777px;top:730px;width:323px;height:196px;background:linear-gradient(135deg,#e8e2d8,#b59b7e)" role="img" aria-label="Photo of an empty room with tall windows"><i class="zoom"></i></div>
</section>

<section class="section testimonials" role="img" aria-label="Photo of a warm lit bedroom interior">
  <div class="quote-card" style="left:96px"><i class="quote-mark"></i><h3>Perspiciatis</h3><p>At vero eos et accusamus et iusto odio dignissimos ducimus qui blanditiis praesentium voluptatum deleniti atque corrupti quos dolores et.</p><div class="quote-foot"><b>Mara Ellison</b><span>28 Jul 2017</span></div></div>
  <div class="quote-card" style="left:437px"><i class="quote-mark"></i><h3>Perspiciatis</h3><p>At vero eos et accusamus et iusto odio dignissimos ducimus qui blanditiis praesentium voluptatum deleniti atque corrupti quos dolores et.</p><div class="quote-foot"><b>Mara Ellison</b><span>28 Jul 2017</span></div></div>
  <div class="quote-card" style="left:777px"><i class="quote-mark"></i><h3>Perspiciatis</h3><p>At vero eos et accusamus et iusto odio dignissimos ducimus qui blanditiis praesentium voluptatum deleniti atque corrupti quos dolores et.</p><div class="quote-foot"><b>Mara Ellison</b><span>28 Jul 2017</span></div></div>
</section>

<section class="section partners">
  <h2 class="section-title">Our Partners</h2>
  <div class="title-dots"><span></span><span></span><span></span></div>
  <div class="partner-row">
    <div class="partner-badge"></div><div class="partner-badge"></div><div class="partner-badge"></div><div class="partner-badge"></div><div class="partner-badge"></div>
  </div>
</section>

<footer class="section footer">
  <div class="foot-col" style="left:96px">
    <h4>Contact Us</h4>
    <div class="label">Company</div><div class="val">12 Harbor Lane, Fairview 4100</div>
    <div class="label">Email address</div><div class="val">info@gildedrealty.example</div>
    <div class="label">Call us</div><div class="val">555-014-7230</div>
  </div>
  <div class="foot-col" style="left:395px">
    <h4>Links</h4>
    <ul><li>What We Do</li><li>What We Offer</li><li>Overview &amp; Rooms</li><li>Our Properties</li><li>Find a Property</li><li>Our Residents</li></ul>
  </div>
  <div class="foot-col" style="left:610px">
    <h4>Legal</h4>
    <ul><li>Support</li><li>FAQ</li><li>Privacy</li><li>Policy</li><li>Terms &amp; Conditions</li><li>Sitemap</li></ul>
  </div>
  <div class="foot-col" style="left:828px">
    <h4>Newsletter</h4>
    <ul><li>For exclusive news and market updates sign</li><li>up for our newsletter.</li></ul>
    <div class="subscribe"><div>Email Address</div><span></span></div>
    <div class="socials"><i></i><i></i><i></i><i></i><i></i></div>
  </div>
  <div class="copyright">© 2017 Copyright <b>GILDED REALTY</b>. All Rights Reserved.</div>
</footer>

</body>
</html>
```